PPT Template for a company that develops software and intellectual property for use by accountants a

We are a boutique firm that develops specialised reporting applications, financial and non-financial reporting content, checklists and other intellectual property for use by business consultants and accounting firms in particular. The applications and content we are creating is strategically focussed and we are required to produce reports and presentations and our current templates are simply not sufficient.

Excel worksheets, graphs and other graphics are regularly embedded into the presentations
We have our logo in 4 colour palettes and will require the winning version to be provided in all 4 colours plus B&W. There is one single logo but the name “Harbor Ledger Pathfinders” is presented in 3 different styles for use depending on the space available etc.
Our clients will typically take our products and rebrand/co brand these (we require them to at least say that there product is “powered by Harbor Ledger Pathfinders” with the logo.
The templates you provide will be used to create marketing presentations, proposal presentations and our standard documents that clients will rebrand or cobrand under license.

A Powerpoint Document Slide Template

Cover page layout, back page, intermediate page heading, in colours and styles based on the logo, title styles, and an intermediate or chapter heading slide style. Many of our presentations contain slides with tables, diagrams, flowcharts and text, including simple lists of bullet points. As above, you will see in our style guide that we have four coloured logos – we would like one version in each. We recommend that we finalise the design using the maroon version and then this be used as the base for the other colour palettes.
Again, the cover should be bold and draw attention but remain professional.

We are looking for something that works in both 4:3 and 16:9 (or two templates please)

We like a clear professional and simple look.

Deliverable: PowerPoint template file (.potx extension) for PowerPoint 2007 with at least a “cover” layout, a “title and content” layout, and a simplified slide layout, as well as “back cover”. Please embed any fonts used.

Industry/Entity Type

Financial

```html
<!DOCTYPE html>
<html lang="en">
<head>
<meta charset="utf-8">
<title>Harbor Ledger Pathfinders – Presentation Template</title>
<link href="https://fonts.googleapis.com/css2?family=Roboto+Condensed:ital,wght@0,300;0,400;0,700;1,300;1,400&display=swap" rel="stylesheet">
<style>
:root{
  --maroon:#b01e23;
  --maroon-dark:#8e1519;
  --charcoal:#333436;
  --mid-grey:#666769;
  --soft-grey:#9a9b9d;
  --pale:#f2f2f2;
  --board:#cfd0d2;
  --white:#ffffff;
}
*{margin:0;padding:0;box-sizing:border-box}
html,body{width:1200px;height:900px;overflow:hidden;background:var(--board);font-family:"Roboto Condensed",Arial,sans-serif}
.slide{position:absolute;width:357px;height:276px;overflow:hidden;background:linear-gradient(180deg,#fff 0%,#f4f4f4 60%,#e9e9e9 100%)}
.slide>*{position:absolute}
.c1{left:36px}.c2{left:406px}.c3{left:779px}
.r1{top:28px}.r2{top:312px}.r3{top:596px}

.header{left:0;top:0;width:100%;height:26px;background:var(--maroon);border-bottom:2px solid #e4e4e4}
.header h2{position:absolute;left:16px;top:6px;color:var(--white);font-weight:300;font-size:14px;letter-spacing:.2px}
.footer-rule{left:16px;right:16px;top:256px;height:1px;background:#b9b9b9}
.footer-mark{left:16px;top:260px;display:flex;align-items:center;gap:3px;font-size:4.5px;color:var(--maroon);line-height:1}
.footer-mark i{display:block;width:8px;height:8px;border-radius:50%;background:var(--charcoal)}
.page-no{right:18px;top:259px;font-size:4px;color:#888}

.wordmark{display:flex;align-items:center;gap:6px;color:var(--maroon);font-weight:400;line-height:1.05}
.wordmark .dot{width:30px;height:30px;border-radius:50%;background:var(--maroon);flex:none}

.body-text{font-size:5px;line-height:1.9;color:#555;text-align:justify}
.body-text p+p{margin-top:6px}
.photo{background:linear-gradient(135deg,#d8d8d8,#8d8d8d 55%,#3f3f3f)}

/* cover */
.cover{background:var(--white)}
.cover .wordmark{left:26px;top:50px;font-size:12.5px}
.red-field{left:0;top:96px;width:100%;height:174px;background:linear-gradient(100deg,var(--maroon-dark),var(--maroon) 60%,#c0262b);border-top-right-radius:30px}
.grey-strip{left:0;bottom:0;width:100%;height:6px;background:#7b7c7e}
.cover-title{right:22px;top:173px;text-align:right;color:var(--white)}
.cover-title h1{font-weight:300;font-size:15.5px;line-height:1.2}
.cover-title p{font-size:7.5px;font-weight:300;margin-top:6px}

/* about 1 */
.team-strip{left:16px;top:37px;width:327px;height:56px}
.lead-caps{left:16px;top:128px;width:102px;font-size:5px;line-height:1.9;color:var(--maroon);text-transform:uppercase}
.about-1 .body-text{left:130px;top:126px;width:206px}

/* about 2 */
.side-sliver{left:0;top:59px;width:18px;height:63px;background:var(--mid-grey)}
.portrait-block{left:18px;top:50px;width:105px;height:72px}
.quote-band{left:123px;top:59px;right:0;height:63px;background:var(--mid-grey);padding:11px 24px 0 26px;color:var(--white);font-style:italic;font-size:5.5px;line-height:2.2;text-align:justify}
.about-2 .body-text{left:150px;top:130px;width:180px;line-height:1.75}

/* chart */
.chart{left:50px;top:50px}
.legend{top:215px;width:80px;font-size:4.2px;line-height:1.5;color:#777;text-align:justify}
.legend b{display:block;font-weight:400;font-size:5px;color:var(--charcoal)}
.legend b::before{content:"";display:inline-block;width:4px;height:4px;margin-right:2px;background:var(--sw)}

/* services */
.service{top:78px;width:100px;text-align:center}
.service .icon{width:42px;height:42px;border-radius:50%;margin:0 auto;display:flex;align-items:center;justify-content:center}
.service h3{margin-top:12px;font-size:8px;font-weight:700;color:var(--maroon)}
.service p{margin-top:4px;font-size:4.8px;line-height:1.5;color:#999}

/* team */
.intro{left:30px;right:30px;top:55px;font-size:4.8px;font-style:italic;font-weight:700;color:#666;text-align:center;line-height:1.9}
.member{top:88px;width:74px;text-align:center}
.member .avatar{width:52px;height:52px;border-radius:50%;border:1px solid var(--maroon);margin:0 auto;padding:2px;background:var(--white)}
.member .avatar span{display:block;width:100%;height:100%;border-radius:50%}
.member h4{margin-top:11px;font-weight:400;font-size:6px;color:#555}
.member em{display:block;font-size:4.5px;color:#666;margin-top:1px}
.member p{margin-top:7px;font-size:4.8px;line-height:2.1;color:#999;text-align:justify}

/* image text */
.split-red{left:0;top:0;width:176px;height:100%;background:var(--maroon)}
.split-photo{left:176px;top:0;right:0;height:100%}
.split-title{left:13px;top:20px;color:var(--white);font-weight:300;font-size:12.5px}
.split-copy{left:22px;top:97px;width:141px;color:var(--white);font-size:4.8px;line-height:1.55;text-align:justify}
.split-copy h5{font-weight:400;font-size:5.2px;margin-bottom:6px}
.split-copy p+p{margin-top:7px}
.split-mark{left:8px;top:253px;color:var(--white);display:flex;align-items:center;gap:4px;font-size:5.2px;line-height:1.05}
.split-mark i{display:block;width:14px;height:14px;border-radius:50%;background:var(--white)}

/* section */
.section{background:var(--maroon)}
.info-badge{left:156px;top:122px;width:44px;height:44px;border-radius:50%;background:var(--white);color:var(--maroon);font:italic 700 30px/44px Georgia,serif;text-align:center}
.section-rule{left:126px;top:174px;width:104px;height:1px;background:#e7a5a7}
.section-title{left:0;width:100%;top:181px;text-align:center;color:var(--white);font-weight:300;font-size:12px}

/* back */
.back{background:var(--white)}
.back .wordmark{left:27px;top:56px;font-size:12.5px}
.back .red-field{top:98px;height:172px}
.thanks{left:30px;top:145px;color:var(--white)}
.thanks h2{font-weight:300;font-size:12px}
.thanks p{font-size:5px;margin-top:1px}
.contacts{left:30px;top:194px;color:var(--white);font-size:5.5px;line-height:1.2;list-style:none}
.contacts li{display:flex;gap:5px;align-items:flex-start;margin-bottom:7px}
.contacts svg{width:7px;height:7px;flex:none}
</style>
</head>
<body>

<!-- Cover -->
<section class="slide cover c1 r1">
  <div class="wordmark"><span class="dot"></span><span>Harbor Ledger<br>Pathfinders</span></div>
  <div class="red-field"></div>
  <div class="cover-title">
    <h1>WELCOME<br>TO OUR PRESENTATION</h1>
    <p>Birmingham, March 25, 2011</p>
  </div>
  <div class="grey-strip"></div>
</section>

<!-- About us: team strip -->
<section class="slide about-1 c2 r1">
  <header class="header"><h2>ABOUT US</h2></header>
  <div class="team-strip photo" role="img" aria-label="Black and white photo strip of business team members"></div>
  <p class="lead-caps">Lorem ipsum dolor sit met consectur adipiscing elit, sed do eiusmod tempor incididunt ut labore et delore magna</p>
  <div class="body-text">
    <p>Lorem ipsum dolor sit amet, consectetur adipisicing elit, sed do eiusmod tempor incididunt ut labore et dolore magna aliqua. Ut enim ad minim veniam, quis nostrud exercitation ullamco laboris nisi ut aliquip ex ea commodo consequat. Duis aute irure dolor in reprehenderit in voluptate velit esse cillum dolore eu fugiat nulla pariatur.</p>
    <p>Lorem ipsum dolor sit amet, consectetur adipisicing elit, sed do eiusmod tempor incididunt ut labore et dolore magna aliqua. Ut enim ad minim veniam, quis nostrud exercitation ullamco laboris nisi ut aliquip ex ea commodo consequat. Duis aute irure dolor in reprehenderit in voluptate velit esse cillum dolore eu</p>
  </div>
  <div class="footer-rule"></div>
  <div class="footer-mark"><i></i><span>Harbor Ledger<br>Pathfinders</span></div>
  <span class="page-no">2</span>
</section>

<!-- About us: quote band -->
<section class="slide about-2 c3 r1">
  <header class="header"><h2>ABOUT US</h2></header>
  <div class="side-sliver"></div>
  <div class="portrait-block photo" role="img" aria-label="Black and white photo of a businesswoman in an office"></div>
  <div class="quote-band">Lorem ipsum dolor sit amet<br>consectetur adipiscing elit, sed do eiusmod tempor incididunt ut labore et dolore magna aliqua. Ut enim ad</div>
  <div class="body-text">
    <p>Lorem ipsum dolor sit amet, consectetur adipisicing elit, sed do eiusmod tempor incididunt ut labore et dolore magna aliqua. Ut enim ad minim veniam, quis nostrud exercitation ullamco laboris nisi ut aliquip ex ea commodo consequat. Duis aute irure dolor in reprehenderit in voluptate velit esse cillum dolore eu fugiat nulla pariatur.</p>
    <p>Lorem ipsum dolor sit amet, consectetur adipisicing elit, sed do eiusmod tempor incididunt ut labore et dolore magna aliqua. Ut enim ad minim veniam, quis nostrud exercitation ullamco laboris nisi ut aliquip ex ea commodo consequat. Duis aute irure dolor in reprehenderit in voluptate velit esse cillum dolore eu</p>
    <p>fugiat nulla pariatur. Excepteur sint occaecat cupidatat non proident, sunt in culpa qui officia deserunt mollit anim id est laborum. Excepteur sint occaecat cupidatat non proident, sunt in consequat. Duis aute irure dolor in reprehenderit</p>
  </div>
  <div class="footer-rule"></div>
  <div class="footer-mark"><i></i><span>Harbor Ledger<br>Pathfinders</span></div>
  <span class="page-no">2</span>
</section>

<!-- About us: chart -->
<section class="slide c1 r2">
  <header class="header"><h2>ABOUT US</h2></header>
  <svg class="chart" width="260" height="160" viewBox="0 0 260 160" font-family="Roboto Condensed, Arial, sans-serif">
    <g stroke="#555" stroke-width=".8">
      <line x1="10" y1="5" x2="10" y2="129"/>
      <line x1="10" y1="129" x2="258" y2="129"/>
      <g stroke-width=".6"><line x1="7" y1="5" x2="10" y2="5"/><line x1="7" y1="25" x2="10" y2="25"/><line x1="7" y1="46" x2="10" y2="46"/><line x1="7" y1="67" x2="10" y2="67"/><line x1="7" y1="88" x2="10" y2="88"/><line x1="7" y1="108" x2="10" y2="108"/></g>
    </g>
    <g>
      <rect x="17" y="39" width="12" height="90" fill="#b01e23"/><rect x="30" y="80" width="12" height="49" fill="#8e8f91"/><rect x="43" y="89" width="12" height="40" fill="#333436"/>
      <rect x="70" y="64" width="12" height="65" fill="#b01e23"/><rect x="83" y="39" width="12" height="90" fill="#8e8f91"/><rect x="96" y="89" width="12" height="40" fill="#333436"/>
      <rect x="123" y="49" width="12" height="80" fill="#b01e23"/><rect x="136" y="91" width="12" height="38" fill="#8e8f91"/><rect x="149" y="72" width="12" height="57" fill="#333436"/>
      <rect x="176" y="52" width="12" height="77" fill="#b01e23"/><rect x="189" y="82" width="12" height="47" fill="#8e8f91"/><rect x="202" y="43" width="12" height="86" fill="#333436"/>
    </g>
    <g fill="#555" font-size="9" font-weight="300" text-anchor="middle">
      <text x="36" y="148">2009</text><text x="89" y="148">2010</text><text x="142" y="148">2011</text><text x="195" y="148">2012</text>
    </g>
  </svg>
  <div class="legend" style="left:38px;--sw:var(--maroon)"><b>LOREM IPSUM</b>Lorem ipsum dolor sit amet, consectetur adipisicing elit, sed do eiusmod tempor incididunt ut labore et dolore magna</div>
  <div class="legend" style="left:138px;--sw:var(--soft-grey)"><b>LOREM IPSUM</b>Lorem ipsum dolor sit amet, consectetur adipisicing elit, sed do eiusmod tempor incididunt ut labore et dolore magna</div>
  <div class="legend" style="left:234px;--sw:var(--charcoal)"><b>LOREM IPSUM</b>Lorem ipsum dolor sit amet, consectetur adipisicing elit, sed do eiusmod tempor incididunt ut labore et dolore magna</div>
  <div class="footer-rule"></div>
  <div class="footer-mark"><i></i><span>Harbor Ledger<br>Pathfinders</span></div>
  <span class="page-no">2</span>
</section>

<!-- About us: services -->
<section class="slide c2 r2">
  <header class="header"><h2>ABOUT US</h2></header>
  <div class="service" style="left:22px">
    <div class="icon" style="background:var(--charcoal)">
      <svg width="22" height="22" viewBox="0 0 22 22"><g fill="#fff"><circle cx="11" cy="11" r="6.5"/><g id="teeth"><rect x="9.5" y="1.5" width="3" height="4"/><rect x="9.5" y="16.5" width="3" height="4"/><rect x="1.5" y="9.5" width="4" height="3"/><rect x="16.5" y="9.5" width="4" height="3"/></g><use href="#teeth" transform="rotate(45 11 11)"/></g><circle cx="11" cy="11" r="2.6" fill="#333436"/></svg>
    </div>
    <h3>OUR SERVICES</h3>
    <p>dolor sit amet, consectetur adipisicing elit, sed do eiusmod tempor incididunt ut labore et dolore magna aliqua. Ut enim ad minim veniam, quis nostrud exercitation ullamco laboris nisi ut aliquip ex ea cesse cillum dolore eu fugiat nulla pariatur.</p>
  </div>
  <div class="service" style="left:128px">
    <div class="icon" style="background:var(--maroon)">
      <svg width="22" height="22" viewBox="0 0 22 22" fill="#fff"><rect x="4" y="13" width="3.5" height="6"/><rect x="9" y="10" width="3.5" height="9"/><rect x="14" y="7" width="3.5" height="12"/><path d="M4 10 L11 5 L13 7 L17 3.5 L17 6 M17 3.5 L14.5 3.5" stroke="#fff" stroke-width="1.4" fill="none"/></svg>
    </div>
    <h3>OUR SERVICES</h3>
    <p>dolor sit amet, consectetur adipisicing elit, sed do eiusmod tempor incididunt ut labore et dolore magna aliqua. Ut enim ad minim veniam, quis nostrud exercitation ullamco laboris nisi ut aliquip ex ea cesse cillum dolore eu fugiat nulla pariatur.</p>
  </div>
  <div class="service" style="left:236px">
    <div class="icon" style="background:var(--soft-grey)">
      <svg width="22" height="22" viewBox="0 0 22 22" fill="none" stroke="#fff" stroke-width="1.4"><rect x="3.5" y="4" width="15" height="10"/><line x1="2" y1="4" x2="20" y2="4"/><path d="M11 14 V17 M8 19 L11 16 L14 19"/><path d="M6 11 L9 8 L11 10 L15 7"/></svg>
    </div>
    <h3>OUR SERVICES</h3>
    <p>dolor sit amet, consectetur adipisicing elit, sed do eiusmod tempor incididunt ut labore et dolore magna aliqua. Ut enim ad minim veniam, quis nostrud exercitation ullamco laboris nisi ut aliquip ex ea cesse cillum dolore eu fugiat nulla pariatur.</p>
  </div>
  <div class="footer-rule"></div>
  <div class="footer-mark"><i></i><span>Harbor Ledger<br>Pathfinders</span></div>
  <span class="page-no">2</span>
</section>

<!-- About us: team -->
<section class="slide c3 r2">
  <header class="header"><h2>ABOUT US</h2></header>
  <p class="intro">dolor sit amet, consectetur adipisicing elit, sed do eiusmod tempor incididunt ut labore et dolore magna aliqua.<br>Ut enim ad minim veniam, quis nostrud exercitation ullamco laboris nisi ut a</p>
  <div class="member" style="left:41px">
    <div class="avatar"><span class="photo" role="img" aria-label="Portrait photo of the president"></span></div>
    <h4>ARTHUR VALE</h4><em>President</em>
    <p>dolor sit amet, consectetur adipiscing elit, sed do eiusmod tempor incididunt ut labore et dolore magna aliqua. Ut enim ad minim veniam, quis nostrud exercitation</p>
  </div>
  <div class="member" style="left:145px">
    <div class="avatar"><span class="photo" role="img" aria-label="Portrait photo of the CEO and founder"></span></div>
    <h4>IRENE SOLIS</h4><em>CEO / Founder</em>
    <p>dolor sit amet, consectetur adipiscing elit, sed do eiusmod tempor incididunt ut labore et dolore magna aliqua. Ut enim ad minim veniam, quis nostrud exercitation</p>
  </div>
  <div class="member" style="left:245px">
    <div class="avatar"><span class="photo" role="img" aria-label="Portrait photo of the vice president"></span></div>
    <h4>GRETA HOLM</h4><em>Vice President</em>
    <p>dolor sit amet, consectetur adipiscing elit, sed do eiusmod tempor incididunt ut labore et dolore magna aliqua. Ut enim ad minim veniam, quis nostrud exercitation</p>
  </div>
  <div class="footer-rule"></div>
  <div class="footer-mark"><i></i><span>Harbor Ledger<br>Pathfinders</span></div>
  <span class="page-no">2</span>
</section>

<!-- Image + text -->
<section class="slide c1 r3">
  <div class="split-red"></div>
  <div class="split-photo photo" role="img" aria-label="Black and white photo of a smiling businesswoman and businessman"></div>
  <h2 class="split-title">IMAGE TEXT</h2>
  <div class="split-copy">
    <h5>LOREM IPSUM DOLOR SIT MET</h5>
    <p>Lorem ipsum dolor sit amet, consectetur adipisicing elit, sed do eiusmod tempor incididunt ut labore et dolore magna aliqua. Ut enim ad minim veniam, quis nostrud exercitation ullamco laboris nisi ut aliquip ex ea commodo consequat. Duis aute irure dolor in reprehenderit in voluptate velit esse cillum dolore eu fugiat nulla pariatur.</p>
    <p>Lorem ipsum dolor sit amet, consectetur adipisicing elit, sed do eiusmod tempor incididunt ut labore et dolore magna aliqua. Ut enim ad minim veniam, quis nostrud exercitation ullamco laboris nisi ut aliquip ex ea commodo consequat. Duis aute irure dolor in reprehenderit in voluptate velit esse cillum dolore eu</p>
  </div>
  <div class="split-mark"><i></i><span>Harbor Ledger<br>Pathfinders</span></div>
</section>

<!-- Section divider -->
<section class="slide section c2 r3">
  <div class="info-badge">i</div>
  <div class="section-rule"></div>
  <h2 class="section-title">SECTION TITLE</h2>
</section>

<!-- Back cover -->
<section class="slide back c3 r3">
  <div class="wordmark"><span class="dot"></span><span>Harbor Ledger<br>Pathfinders</span></div>
  <div class="red-field"></div>
  <div class="thanks"><h2>THANK YOU</h2><p>FOR YOUR TIME</p></div>
  <ul class="contacts">
    <li><svg viewBox="0 0 8 8"><circle cx="4" cy="4" r="4" fill="#fff"/><path d="M4 1.8 C2.9 1.8 2.3 2.6 2.3 3.4 C2.3 4.5 4 6.3 4 6.3 S5.7 4.5 5.7 3.4 C5.7 2.6 5.1 1.8 4 1.8Z" fill="#b01e23"/></svg><span>4120 Quarry Bend Road Ste 300<br>Fairhaven, Ohio 44021</span></li>
    <li><svg viewBox="0 0 8 8"><circle cx="4" cy="4" r="4" fill="#fff"/><path d="M2.4 2.2 L3.3 2 L3.8 3.2 L3.2 3.6 C3.5 4.3 3.8 4.6 4.4 4.9 L4.8 4.3 L6 4.8 L5.8 5.7 C4 5.8 2.3 4.1 2.4 2.2Z" fill="#b01e23"/></svg><span>1.800.555.0142</span></li>
    <li><svg viewBox="0 0 8 8"><circle cx="4" cy="4" r="4" fill="#fff"/><rect x="2" y="2.7" width="4" height="2.8" fill="none" stroke="#b01e23" stroke-width=".6"/><path d="M2 2.7 L4 4.3 L6 2.7" fill="none" stroke="#b01e23" stroke-width=".6"/></svg><span>support@harborledgerpf.com</span></li>
    <li><svg viewBox="0 0 8 8"><circle cx="4" cy="4" r="4" fill="#fff"/><circle cx="4" cy="4" r="2.2" fill="none" stroke="#b01e23" stroke-width=".6"/><path d="M1.8 4 H6.2 M4 1.8 C3 3 3 5 4 6.2 M4 1.8 C5 3 5 5 4 6.2" fill="none" stroke="#b01e23" stroke-width=".5"/></svg><span>www.harborledgerpf.com</span></li>
  </ul>
  <div class="grey-strip"></div>
</section>

</body>
</html>
```